Real Estate Business Cards

Looking for a clean, sharp and professional look for our Real Estate investment Fund that invests in Multi Family Apartment buildings.

Target Market(s)

Real Estate Fund

Industry/Entity Type

Real Estate

Contact Information for Business Card

Company Description: Real Estate Investment Fund
Company Name: RKW Holdings
Name: Marcus Olvane
Cell: (917) 482-0657
Email: marcus@rkwholdings-example.com
Website: www.rkwholdings-example.com
Address: 418, 9th Street, Brooklyn NY 11218

Colors

Designer to choose colors to be used in the design.

Requirements
Nice to have
• Colors to match logo

```html
<!DOCTYPE html>
<html lang="en">
<head>
<meta charset="utf-8">
<title>RKW Holdings – Business Card</title>
<link rel="stylesheet" href="https://fonts.googleapis.com/css2?family=Barlow+Condensed:wght@600&family=Montserrat:wght@400;500&display=swap">
<style>
  :root {
    --backdrop: #2c2c2c;
    --card: #1f1f20;
    --brand-grey: #8a8b8d;
    --accent: #1b7fc0;
    --ink: #f2f2f2;
    --rule: #d8d8d8;
  }
  * { box-sizing: border-box; margin: 0; padding: 0; }
  html, body {
    width: 1200px; height: 901px; overflow: hidden;
    background: var(--backdrop);
  }
  .canvas {
    width: 1200px; height: 901px;
    display: flex; flex-direction: column; align-items: center; justify-content: center;
    gap: 40px;
  }
  .card {
    position: relative;
    width: 700px; height: 400px;
    background: var(--card);
    box-shadow: 0 10px 24px rgba(0,0,0,.35);
  }
  /* Front */
  .card--front { display: flex; align-items: center; justify-content: center; gap: 22px; }
  .brand-mark { width: 54px; height: 54px; border: 6px solid var(--brand-grey); }
  .brand-name {
    font-family: "Montserrat", sans-serif; font-weight: 500;
    font-size: 40px; letter-spacing: 4px; text-transform: uppercase;
    color: var(--brand-grey);
  }
  /* Back */
  .identity {
    position: absolute; left: 0; right: 0; top: 128px;
    display: flex; align-items: center; justify-content: center;
    gap: 20px;
  }
  .holder-name {
    font-family: "Barlow Condensed", sans-serif; font-weight: 600;
    font-size: 46px; letter-spacing: 1px; text-transform: uppercase;
    color: var(--accent); line-height: 1; white-space: nowrap;
  }
  .divider {
    flex: none;
    width: 2px; height: 86px; background: var(--rule);
  }
  .contact-list {
    list-style: none;
    font-family: "Montserrat", sans-serif; font-size: 14px; color: var(--ink);
  }
  .contact-list li { display: flex; align-items: center; gap: 10px; height: 26px; white-space: nowrap; }
  .contact-list svg { width: 15px; height: 15px; flex: none; }
  .contact-list .highlight { color: var(--accent); }
  .address {
    position: absolute; left: 0; right: 0; top: 316px; text-align: center;
    font-family: "Montserrat", sans-serif; font-size: 16px; color: var(--ink);
  }
</style>
</head>
<body>
<main class="canvas">
  <section class="card card--front" aria-label="Card front">
    <span class="brand-mark"></span>
    <span class="brand-name">RKW Holdings</span>
  </section>

  <section class="card card--back" aria-label="Card back">
    <div class="identity">
      <h1 class="holder-name">Marcus Olvane</h1>
      <span class="divider"></span>
      <ul class="contact-list">
        <li>
          <svg viewBox="0 0 24 24" aria-hidden="true"><path fill="var(--accent)" d="M6.6 10.8a15.1 15.1 0 0 0 6.6 6.6l2.2-2.2c.3-.3.7-.4 1-.2 1.1.4 2.3.6 3.6.6.6 0 1 .4 1 1V20c0 .6-.4 1-1 1C10.6 21 3 13.4 3 4c0-.6.4-1 1-1h3.5c.6 0 1 .4 1 1 0 1.3.2 2.5.6 3.6.1.3 0 .7-.2 1z"/></svg>
          <span>(917) 482-0657</span>
        </li>
        <li>
          <svg viewBox="0 0 24 24" aria-hidden="true"><rect x="2" y="5" width="20" height="14" rx="1.5" fill="var(--accent)"/><path d="M3 6.5l9 6.5 9-6.5" fill="none" stroke="var(--card)" stroke-width="1.6"/></svg>
          <span>marcus@rkwholdings-example.com</span>
        </li>
        <li>
          <svg viewBox="0 0 24 24" aria-hidden="true"><circle cx="12" cy="12" r="10" fill="var(--accent)"/><path d="M2 12h20M12 2c3 3 3 17 0 20M12 2c-3 3-3 17 0 20" fill="none" stroke="var(--card)" stroke-width="1.4"/></svg>
          <span>www.<span class="highlight">rkwholdings-example</span>.com</span>
        </li>
      </ul>
    </div>
    <p class="address">418, 9th Street, Brooklyn NY 11218</p>
  </section>
</main>
</body>
</html>
```